I am seeking a book cover design for a new book series. The book deals with life and the principles and essentials that we must have in our lives in order to be happy and have a successful life. Some of the tenets will include 'Spirit' Believe' 'Trust' 'Harmony' 'Family' etc...

I would like to have some natural scene in the background (i.e. water, moutains, forest...that is a ZEN or purity feel)

The '24' should be pronounced in the title in within the foreground of the book cover.

I am open to colors but would like the coloring to emphasize attention. Colors such as forest greens, peaches, pomegranites, are ones that come to mind but i am completely open since it must fit the design.

I will also be looking to do a web design and other additional logos/designs in the coming months so this is a long term opportunity with the right design and communication. I look forward to working with a great partner on this project.

Reason: I am extending the deadline to allow designers who inquired to get their designs submitted. Also to allow several designers to submit changes to their design.

Target Market(s)

Spiritual - Age range 18-80 - Forward Thinkers - Degreed - All cultures and religions

Industry/Entity Type

Communication

Requirements
Must have
• The title 'The Amber Lantern Road'

My Name as the Author: Dovan Pruett

the thoughts should also include a backcover copy consistent with the front and a theme design for the Series.
The book is expected to be 5 1/2 x 8 1/2"
Nice to have
• The book will be released in a series format as well as the entire Amber Lantern. As a suggestion, the books released as part of an individual essential would have the name of that essential referenced on the book. Example (BELEIVE). You may take that into consideration when designing for he cover. Thank you.

```html
<!DOCTYPE html>
<html lang="en">
<head>
<meta charset="utf-8">
<title>The Amber Lantern Road — Book Cover Spread</title>
<link rel="stylesheet" href="https://fonts.googleapis.com/css2?family=Cormorant+Garamond:wght@400;500&family=Marcellus&family=EB+Garamond&family=Arimo:wght@700&family=Questrial&display=swap">
<style>
  :root {
    --forest-band: #3e5228;
    --leaf-light: #b9d66a;
    --leaf-mid: #6f9a2e;
    --leaf-deep: #2f4a1a;
    --back-light: #6f8455;
    --back-deep: #3b4d2a;
    --amber: #f28a1e;
    --ivory: #ffffff;
    --ink: #2a2a2a;
    --label-veil: rgba(255, 255, 255, 0.78);
  }
  * { margin: 0; padding: 0; box-sizing: border-box; }
  html, body { width: 1200px; height: 850px; overflow: hidden; background: var(--forest-band); }
  .spread { position: relative; width: 1200px; height: 850px; overflow: hidden; }

  .title-band {
    position: absolute; left: 0; top: 0; width: 1200px; height: 202px;
    background: var(--forest-band);
  }
  .back-scene {
    position: absolute; left: 0; top: 202px; width: 648px; height: 648px;
    background:
      radial-gradient(ellipse at 30% 30%, rgba(160,180,130,0.45), transparent 60%),
      linear-gradient(180deg, var(--back-light) 0%, #556b3c 45%, var(--back-deep) 100%);
  }
  .front-scene {
    position: absolute; left: 648px; top: 200px; width: 552px; height: 650px;
    background:
      radial-gradient(ellipse at 35% 20%, rgba(240,250,200,0.85), transparent 45%),
      radial-gradient(ellipse at 70% 70%, rgba(150,200,60,0.6), transparent 55%),
      linear-gradient(180deg, var(--leaf-light) 0%, var(--leaf-mid) 50%, var(--leaf-deep) 100%);
  }

  /* Back cover copy */
  .back-copy {
    position: absolute; left: 114px; top: 272px; width: 345px;
    font-family: "EB Garamond", Georgia, serif;
    font-size: 16.5px; line-height: 30.6px; color: var(--ivory);
  }
  .back-copy p + p { margin-top: 30px; }

  /* Spine */
  .spine-title {
    position: absolute; left: 406px; top: 236px; width: 380px; height: 72px;
    transform: rotate(-90deg); transform-origin: center;
    display: flex; align-items: center; justify-content: center;
    white-space: nowrap; color: var(--ivory);
  }
  .spine-title .title-article {
    font-family: "Marcellus", serif; font-size: 13px; letter-spacing: 1px;
    writing-mode: vertical-rl; transform: rotate(180deg); margin-right: 4px;
  }
  .spine-title .title-key {
    font-family: "Cormorant Garamond", serif; font-size: 52px; line-height: 1;
    color: var(--amber); margin-right: 8px;
  }
  .spine-title .title-rest { font-family: "Marcellus", serif; line-height: 1; }
  .spine-title .title-rest span { display: block; }
  .spine-title .rest-top { font-size: 22px; letter-spacing: 1px; }
  .spine-title .rest-bottom { font-size: 32px; }

  .spine-author {
    position: absolute; left: 498px; top: 698px; width: 200px; height: 24px;
    transform: rotate(-90deg); transform-origin: center;
    font-family: "Arimo", Arial, sans-serif; font-weight: 700; font-size: 18px;
    color: var(--ivory); text-align: center; white-space: nowrap; line-height: 24px;
  }

  /* Front cover title */
  .front-title {
    position: absolute; left: 680px; top: 52px; height: 130px;
    display: flex; align-items: flex-end; gap: 10px;
    color: var(--ivory); white-space: nowrap; font-weight: 400;
  }
  .front-title .title-article {
    font-family: "Marcellus", serif; font-size: 26px; line-height: 1;
    writing-mode: vertical-rl; transform: rotate(180deg);
    align-self: flex-start; margin-top: 6px;
  }
  .front-title .title-key {
    font-family: "Cormorant Garamond", serif; font-weight: 500; font-size: 94px; line-height: 0.9;
    color: var(--amber); margin-bottom: 8px;
  }
  .front-title .title-rest { display: flex; flex-direction: column; font-family: "Marcellus", serif; line-height: 1; }
  .front-title .rest-top { font-size: 35px; letter-spacing: 1px; }
  .front-title .rest-bottom { font-size: 54px; margin-top: 4px; }

  .essential-label {
    position: absolute; left: 966px; top: 238px; width: 234px; height: 31px;
    background: var(--label-veil);
    font-family: "Questrial", sans-serif; font-size: 18px; letter-spacing: 2.5px;
    color: var(--ink); line-height: 31px; padding-left: 36px;
  }
  .front-author {
    position: absolute; left: 966px; top: 764px;
    font-family: "Arimo", Arial, sans-serif; font-weight: 700; font-size: 22px;
    color: var(--ivory); white-space: nowrap;
  }
</style>
</head>
<body>
<main class="spread">
  <div class="title-band"></div>
  <div class="back-scene" role="img" aria-label="Muted, softly faded photograph of a green forest floor with tall trees"></div>
  <div class="front-scene" role="img" aria-label="Sunlit photograph of a lush green forest with tall trunks and a path through ferns"></div>

  <section class="back-copy">
    <p>Lorem ipsum dolor sit amet, consectetur adipiscing elit. Nullam fermentum imperdiet bibendum. Nulla facilisi. Nunc leo diam, sollicitudin fermentum venenatis ut, gravida eu odio. Nullam posuere pellentesque mauris et blandit. Duis eu est ut ipsum faucibus pellentesque. Vivamus ut commodo quam. Vivamus vel libero dolor. Nulla dapibus auctor lacus quis malesuada.</p>
    <p>Proin accumsan tincidunt odio, eget ullamcorper turpis volutpat in. Proin enim tellus, accumsan non rhoncus ut, condimentum sit amet mi. Duis ligula nisl, interdum vel venenatis sed, gravida non justo. Morbi convallis laoreet dignissim.</p>
  </section>

  <div class="spine-title">
    <span class="title-article">THE</span>
    <span class="title-key">Amber</span>
    <span class="title-rest"><span class="rest-top">LANTERN</span><span class="rest-bottom">ROAD</span></span>
  </div>
  <div class="spine-author">Dovan Pruett</div>

  <h1 class="front-title">
    <span class="title-article">THE</span>
    <span class="title-key">Amber</span>
    <span class="title-rest"><span class="rest-top">LANTERN</span><span class="rest-bottom">ROAD</span></span>
  </h1>

  <div class="essential-label">Harmony</div>
  <div class="front-author">Dovan Pruett</div>
</main>
</body>
</html>
```